We are a doctors medical practice
I need the business card to be eye catching and memorable,
to reflect professionalism, yet also warmth and care

the numbers need to be easy to see, for the elderly

and the logo also in a location that is large enough to see and be eye catching

Back of card:
opening hours:
Mon- Fri 8.30am to 6pm
Sat 9am to 4pm

rows for appontments, date and time
Updates

HiĀ 

Modification to company name

BRAMBLEWOOD HOME HEALTH MEDICAL PRACTICE

Thanks
Clara

Reason: I am look for a unique design that also fulfils the design brief

I have attempted to post a .eps and .ai file of the logo

Target Market(s)

needs to appeal to the majority, mainly adults

Industry/Entity Type

Medical

Contact Information for Business Card

company name: Bramblewood Home Health Medical Practice
Name: Dr Clara Ostrowski-Vey
Qualifications: MBBS, Bsci(med), FRACGP, DCH, SH&FPA, Dip Derm
Address: Shop 3/41-43 Calder Rd, Brookvale 2371
Ph: 02 9418 3052
Fax: 02 9436 8120

Requirements
Nice to have
• I like balance
gold/ silver incorporated, as well as the other colours in the logo- but not limited to these colours
a "medical" feel
Should not have
• dark or strong colours

```html
<!DOCTYPE html>
<html lang="en">
<head>
<meta charset="utf-8">
<title>Bramblewood Home Health Medical Practice – Business Card</title>
<link rel="stylesheet" href="https://fonts.googleapis.com/css2?family=Open+Sans:wght@400;600;700&display=swap">
<style>
  :root {
    --navy: #173a6b;
    --green: #22b14c;
    --white: #ffffff;
    --paper-grey: #e4e5e7;
    --ink: #2a2a2a;
    --dot: #555555;
    --emblem-blue: #8fb3d9;
    --emblem-green: #7cc79a;
    --emblem-lilac: #c59ad6;
    --backdrop: #eef0f2;
  }
  * { box-sizing: border-box; margin: 0; padding: 0; }
  html, body {
    width: 1200px; height: 900px; overflow: hidden;
    background: var(--backdrop);
    font-family: "Open Sans", Arial, sans-serif;
  }
  .sheet {
    width: 1200px; height: 900px;
    display: flex; flex-direction: column; align-items: center; justify-content: center;
    gap: 30px;
  }
  .card {
    position: relative;
    width: 660px; height: 403px;
    overflow: hidden;
    box-shadow: 0 6px 18px rgba(0,0,0,0.18);
  }

  /* Front */
  .card-front { background: var(--navy); }
  .front-header {
    position: absolute; left: 0; top: 0; width: 100%; height: 112px;
    background: var(--white);
    display: flex; align-items: center; gap: 16px; padding: 0 40px 0 26px;
  }
  .brand-dot {
    width: 62px; height: 62px; border-radius: 50%; flex: none;
    background: radial-gradient(circle at 50% 45%, #ffffff 0%, #e8eef7 45%, var(--emblem-blue) 100%);
  }
  .brand-name {
    color: var(--navy);
    font-weight: 700; font-size: 19px; letter-spacing: 0.2px;
    white-space: nowrap;
  }
  .front-emblem {
    position: absolute; left: 36px; top: 138px;
    width: 258px; height: 258px; border-radius: 50%;
    background:
      radial-gradient(circle at 62% 72%, rgba(197,154,214,0.75) 0%, rgba(197,154,214,0) 38%),
      radial-gradient(circle at 40% 40%, rgba(230,236,244,0.55) 0%, rgba(230,236,244,0) 50%),
      linear-gradient(160deg, #9db1cc 0%, #7d96b9 100%);
    box-shadow: 0 0 0 9px rgba(124,199,154,0.55), 0 0 0 16px rgba(52,120,200,0.45);
  }
  .doctor {
    position: absolute; left: 350px; top: 140px; color: var(--white);
  }
  .doctor-name { font-weight: 700; font-size: 24px; line-height: 1.2; }
  .doctor-quals { font-size: 13px; line-height: 1.45; margin-top: 6px; }
  .contact {
    margin-top: 34px; font-size: 16px; font-weight: 600; line-height: 1.45;
    display: grid; grid-template-columns: 78px 14px auto;
  }

  /* Back */
  .card-back {
    background: linear-gradient(180deg, var(--white) 20%, var(--paper-grey) 100%);
  }
  .hours-band {
    position: absolute; left: 0; top: 0; width: 100%; height: 96px;
    background: var(--green); color: var(--white);
    display: flex; align-items: flex-start; padding: 16px 0 0 26px;
    font-weight: 600; font-size: 25px; line-height: 1.25;
  }
  .hours-label { margin-right: 22px; }
  .hours-times span { display: block; }
  .hours-times span + span { padding-left: 22px; }
  .back-emblem {
    position: absolute; right: 58px; top: 150px;
    width: 230px; height: 230px; border-radius: 50%;
    background:
      radial-gradient(circle at 55% 75%, rgba(197,154,214,0.22) 0%, rgba(197,154,214,0) 40%),
      radial-gradient(circle, rgba(255,255,255,0) 55%, rgba(124,199,154,0.18) 66%, rgba(143,179,217,0.28) 100%);
  }
  .appointments {
    position: absolute; left: 26px; right: 26px; top: 112px; bottom: 20px;
  }
  .appointments-head {
    display: flex; justify-content: space-between;
    font-size: 16px; font-weight: 600; color: var(--ink);
  }
  .appointment-rows { list-style: none; margin-top: 6px; }
  .appointment-rows li {
    height: 31px; border-bottom: 2px dotted var(--dot);
  }
</style>
</head>
<body>
<main class="sheet">
  <section class="card card-front">
    <header class="front-header">
      <div class="brand-dot"></div>
      <h1 class="brand-name">BRAMBLEWOOD HOME HEALTH MEDICAL PRACTICE</h1>
    </header>
    <div class="front-emblem" role="img" aria-label="Large faint practice emblem in soft blue, green and lilac"></div>
    <div class="doctor">
      <h2 class="doctor-name">Dr Clara Ostrowski-Vey</h2>
      <p class="doctor-quals">MBBS, Bsci(med), FRACGP,<br>DCH, SH&amp;FPA, Dip Derm</p>
      <div class="contact">
        <span>Tel</span><span>:</span><span>02 9418 3052</span>
        <span>Fax</span><span>:</span><span>02 9436 8120</span>
        <span>Address</span><span>:</span><span>Shop 3/41-43 Calder Rd,<br>Brookvale 2371</span>
      </div>
    </div>
  </section>

  <section class="card card-back">
    <div class="hours-band">
      <span class="hours-label">OPENING HOURS:</span>
      <p class="hours-times"><span>Mon- Fri 8.30am to 6pm</span><span>Sat 9am to 4pm</span></p>
    </div>
    <div class="back-emblem" role="img" aria-label="Faint practice emblem watermark"></div>
    <div class="appointments">
      <div class="appointments-head"><span>Appontments</span><span>Date &amp; Time</span></div>
      <ul class="appointment-rows">
        <li></li><li></li><li></li><li></li><li></li><li></li><li></li><li></li>
      </ul>
    </div>
  </section>
</main>
</body>
</html>
```